Brisbane IT support business needs our first website

Hi All,

We are after a new website design for our IT solutions and support business.The business name is Kestrel Harbour Computing Services, or KHCS for short. We provide a range of solutions and services within the IT space.

I would like to utilize the two colours in our business logo I have uploaded.

I understand this is initially for the design only aspect of the site, but I would like to engage the winner to finish coding the website and finalize after also.

Target Market(s)

Other businesses owners and home users.

Industry/Entity Type

Business

Requirements
Must have
• Nice clean and functional design utilizing our business colours from the logo.

```html
<!DOCTYPE html>
<html lang="en">
<head>
<meta charset="utf-8">
<title>Kestrel Harbour Computing Services</title>
<link href="https://fonts.googleapis.com/css2?family=Open+Sans:wght@300;400;600;700&display=swap" rel="stylesheet">
<style>
:root{
  --orange:#f47b20;
  --navy:#0d3c5f;
  --navy-dark:#082f4c;
  --text:#555555;
  --muted:#777777;
  --rule:#e2e2e2;
  --footer:#efefef;
  --band:#1b2126;
  --white:#ffffff;
}
*{margin:0;padding:0;box-sizing:border-box}
html,body{width:1200px;height:2206px;overflow:hidden;background:var(--white)}
body{position:relative;font-family:Arial,Helvetica,sans-serif;color:var(--text)}
.abs{position:absolute}
.heading{font-family:'Open Sans',Arial,sans-serif}

/* header */
.site-header{left:0;top:0;width:1200px;height:108px;background:var(--white)}
.brand{left:170px;top:13px;display:flex;align-items:center;gap:14px}
.brand-mark{width:82px;height:82px;border-radius:50%;background:var(--navy)}
.brand-name{font-family:'Open Sans',Arial,sans-serif;font-weight:700;font-size:40px;color:var(--orange);letter-spacing:1px}
.contact-item{top:30px;display:flex;align-items:center;gap:14px}
.contact-item svg{width:42px;height:42px}
.contact-label{font-family:'Open Sans',Arial,sans-serif;font-size:13px;color:#888;text-transform:uppercase;line-height:16px}
.contact-value{font-family:'Open Sans',Arial,sans-serif;font-size:16px;font-weight:600;color:var(--orange);line-height:22px}

.main-nav{left:0;top:108px;width:1200px;height:44px;background:var(--navy)}
.main-nav a{position:absolute;top:0;line-height:44px;font-size:11px;color:var(--white);text-decoration:none;text-transform:uppercase;transform:translateX(-50%)}

/* hero */
.hero{left:0;top:152px;width:1200px;height:517px;background:linear-gradient(100deg,#c9d3dc 0%,#e9edf0 35%,#dfe5ea 60%,#f4f6f8 100%)}
.hero-title{left:615px;top:300px;font-weight:700;font-size:42px;color:var(--orange);line-height:50px;letter-spacing:1px}
.hero-sub{left:615px;top:359px;font-weight:700;font-size:24px;color:var(--navy);line-height:32px;letter-spacing:.5px}
.hero-tag{left:615px;top:396px;font-weight:300;font-size:29px;color:#1f2a33;line-height:38px}
.hero-arrow{left:1138px;top:372px}

/* partners */
.partners{left:0;top:669px;width:1200px;height:90px;border-bottom:1px solid var(--rule)}
.partner{top:29px;width:88px;height:32px;border-radius:4px;background:#d8dde2;transform:translateX(-50%)}

/* welcome */
.welcome-title{left:0;width:1200px;text-align:center;top:800px;font-weight:600;font-size:30px;color:var(--orange)}
.welcome-sub{left:0;width:1200px;text-align:center;top:842px;font-weight:700;font-size:19px;color:var(--navy);letter-spacing:.3px}
.intro{left:170px;top:908px;width:410px;font-size:11px;line-height:22px;color:var(--muted)}
.point{left:170px;width:420px;display:flex;gap:18px;align-items:flex-start}
.point-icon{flex:none;width:42px;height:42px;border-radius:50%;background:var(--orange);display:flex;align-items:center;justify-content:center}
.point p{font-size:11px;line-height:22px;color:#444;padding-top:2px}
.welcome-photo{left:619px;top:913px;width:409px;height:279px;background:linear-gradient(135deg,#e8ecef,#9aa4ad 55%,#3d444b)}
.divider{left:170px;width:858px;height:1px;background:var(--rule)}

/* services */
.section-label{left:170px;top:1272px;font-weight:600;font-size:16px;color:var(--orange)}
.service{top:1320px;width:197px}
.service-photo{width:197px;height:132px}
.service h3{margin-top:16px;font-family:'Open Sans',Arial,sans-serif;font-weight:600;font-size:14px;color:var(--orange)}
.service p{margin-top:6px;font-size:11px;line-height:22px;color:var(--muted)}

/* get in touch */
.full-rule{left:0;width:1200px;height:1px;background:var(--rule)}
.touch-title{left:196px;top:1625px;font-weight:600;font-size:16px;color:var(--orange)}
.touch-text{left:196px;top:1651px;font-size:14px;color:var(--muted)}
.btn{left:873px;top:1630px;width:132px;height:37px;background:var(--orange);color:var(--white);font-family:'Open Sans',Arial,sans-serif;font-weight:600;font-size:12px;line-height:37px;text-align:center;text-transform:uppercase;border-radius:2px}

/* testimonials */
.testimonials{left:0;top:1695px;width:1200px;height:381px;background:linear-gradient(180deg,#2a3137,#161b1f 70%,#101417)}
.test-title{left:0;width:1200px;text-align:center;top:1752px;font-weight:700;font-size:19px;color:var(--white)}
.quote{left:266px;top:1818px;width:668px;text-align:center;font-size:11.5px;line-height:23px;color:#e6e6e6}
.qmark{font-family:Georgia,serif;font-size:40px;color:#bbbbbb}
.avatar{left:474px;top:1943px;width:82px;height:82px;border-radius:50%;background:linear-gradient(#c6ccd1,#8b9298);border:3px solid var(--white)}
.author{left:578px;top:1960px;font-size:13px;color:#dddddd;line-height:24px}
.author em{font-style:italic}
.slide-arrow{top:1862px}

/* footer */
.site-footer{left:0;top:2076px;width:1200px;height:130px;background:var(--footer)}
.footer-brand{left:170px;top:2118px;display:flex;align-items:center;gap:10px}
.footer-brand .brand-mark{width:48px;height:48px}
.footer-brand .brand-name{font-size:24px}
.footer-sep{left:320px;top:2116px;width:1px;height:50px;background:#cfcfcf}
.footer-links{left:345px;top:2120px;font-size:10.5px;color:#555;word-spacing:2px}
.footer-links span{color:#999;margin:0 9px}
.copyright{left:345px;top:2148px;font-size:10.5px;color:#555}
.social{top:2123px;width:38px;height:38px;border-radius:50%;border:1.5px solid #a8a8a8}
</style>
</head>
<body>

<header class="abs site-header">
  <div class="abs brand" style="position:absolute">
    <div class="brand-mark"></div>
    <div class="brand-name">KHCS</div>
  </div>
  <div class="abs contact-item" style="left:659px">
    <svg viewBox="0 0 42 42"><circle cx="21" cy="21" r="19.5" fill="none" stroke="#8a8a8a" stroke-width="2"/><path d="M15 13c1-1 2.5-1 3 .5l1.2 3c.3 1-.3 1.7-1 2.2 1 2.3 2.8 4.1 5.1 5.1.5-.7 1.2-1.3 2.2-1l3 1.2c1.5.5 1.5 2 .5 3-2 2.2-5 1.8-8.5-1.2S12.8 15 15 13z" fill="#8a8a8a"/></svg>
    <div><div class="contact-label">Call us :</div><div class="contact-value">( 2140 ) 555 018</div></div>
  </div>
  <div class="abs contact-item" style="left:867px">
    <svg viewBox="0 0 42 42"><circle cx="21" cy="21" r="19.5" fill="none" stroke="#8a8a8a" stroke-width="2"/><rect x="12" y="15" width="18" height="12" rx="1" fill="#8a8a8a"/><path d="M12.5 15.5 21 22l8.5-6.5" fill="none" stroke="#fff" stroke-width="1.4"/></svg>
    <div><div class="contact-label">Email us :</div><div class="contact-value">info@khcs.net</div></div>
  </div>
</header>

<nav class="abs main-nav">
  <a style="left:193px">Home</a>
  <a style="left:297px">About Us</a>
  <a style="left:410px">Services</a>
  <a style="left:531px">Technology</a>
  <a style="left:639px">FAQ</a>
  <a style="left:735px">Support</a>
  <a style="left:860px">Testimonials</a>
  <a style="left:993px">Contact Us</a>
</nav>

<section class="abs hero" role="img" aria-label="Photo of two colleagues working together at a laptop in a bright office"></section>
<div class="abs heading hero-title">KESTREL HARBOUR</div>
<div class="abs heading hero-sub">COMPUTING SERVICES</div>
<div class="abs heading hero-tag">IT solutions and support company</div>
<svg class="abs hero-arrow" width="22" height="80" viewBox="0 0 22 80"><path d="M2 2l18 38L2 78" fill="none" stroke="#ffffff" stroke-width="1.5"/></svg>

<section class="abs partners" aria-label="Partners">
  <div class="abs partner" style="left:243px"></div>
  <div class="abs partner" style="left:385px"></div>
  <div class="abs partner" style="left:526px"></div>
  <div class="abs partner" style="left:669px"></div>
  <div class="abs partner" style="left:819px"></div>
  <div class="abs partner" style="left:963px"></div>
</section>

<h1 class="abs heading welcome-title">WELCOME TO</h1>
<h2 class="abs heading welcome-sub">KESTREL HARBOUR COMPUTING SERVICES</h2>

<p class="abs intro">Lorem Ipsum is simply dummy text of the printing and typesetting industry. Lorem Ipsum has been the industry's standard dummy text ever since the 1500s, when an unknown printer...</p>

<div class="abs point" style="top:996px">
  <div class="point-icon"><svg width="18" height="14" viewBox="0 0 18 14"><path d="M2 13c0-5 3-8 10-8V1l5 5-5 5V8C7 8 4 9 2 13z" fill="none" stroke="#fff" stroke-width="1.4" stroke-linejoin="round"/></svg></div>
  <p>Lorem Ipsum is simply dummy text of the printing and typesetting industry. Lorem Ipsum has been the industry's.</p>
</div>
<div class="abs point" style="top:1073px">
  <div class="point-icon"><svg width="18" height="14" viewBox="0 0 18 14"><path d="M2 13c0-5 3-8 10-8V1l5 5-5 5V8C7 8 4 9 2 13z" fill="none" stroke="#fff" stroke-width="1.4" stroke-linejoin="round"/></svg></div>
  <p>Lorem Ipsum is simply dummy text of the printing and typesetting industry.</p>
</div>
<div class="abs point" style="top:1145px">
  <div class="point-icon"><svg width="18" height="14" viewBox="0 0 18 14"><path d="M2 13c0-5 3-8 10-8V1l5 5-5 5V8C7 8 4 9 2 13z" fill="none" stroke="#fff" stroke-width="1.4" stroke-linejoin="round"/></svg></div>
  <p>Lorem Ipsum is simply dummy text of the printing and typesetting industry. has been the industry's.</p>
</div>

<div class="abs welcome-photo" role="img" aria-label="Photo of three business people reviewing work on a laptop"></div>

<div class="abs divider" style="top:1242px"></div>

<h2 class="abs heading section-label">SERVICES</h2>

<article class="abs service" style="left:170px">
  <div class="service-photo" role="img" aria-label="Photo of two colleagues in a meeting" style="background:linear-gradient(135deg,#e9eaec,#b9b3ad 60%,#55524f)"></div>
  <h3>SERVICES 01</h3>
  <p>Lorem Ipsum is simply dummy text of the printing and typesetting industry. the industry's standard dummy...</p>
</article>
<article class="abs service" style="left:391px">
  <div class="service-photo" role="img" aria-label="Photo of a woman using a digital touch interface" style="background:linear-gradient(135deg,#7fc6e6,#2d8fc0 55%,#0f5f8c)"></div>
  <h3>SERVICES 02</h3>
  <p>Lorem Ipsum is simply dummy text of the printing and typesetting industry. the industry's standard dummy...</p>
</article>
<article class="abs service" style="left:612px">
  <div class="service-photo" role="img" aria-label="Photo of a woman holding a light bulb and a tablet" style="background:linear-gradient(135deg,#2a1f1a,#6b4a3a 55%,#b59a88)"></div>
  <h3>SERVICES 03</h3>
  <p>Lorem Ipsum is simply dummy text of the printing and typesetting industry. the industry's standard dummy...</p>
</article>
<article class="abs service" style="left:832px">
  <div class="service-photo" role="img" aria-label="Photo of a support agent wearing a headset" style="background:linear-gradient(135deg,#eef0f2,#c9cdd1 55%,#9ea3a8)"></div>
  <h3>SERVICES 04</h3>
  <p>Lorem Ipsum is simply dummy text of the printing and typesetting industry. the industry's standard dummy...</p>
</article>

<div class="abs full-rule" style="top:1602px"></div>
<h2 class="abs heading touch-title">GET IN TOUCH</h2>
<p class="abs touch-text">Lorem Ipsum is simply dummy text of the printing and typesetting industry.&nbsp; the industry's standard dummy...</p>
<a class="abs btn">Contact Here</a>

<section class="abs testimonials" role="img" aria-label="Dark background photo of a computer keyboard"></section>
<h2 class="abs heading test-title">TESTIMONIALS</h2>
<div class="abs qmark" style="left:236px;top:1790px">&ldquo;</div>
<p class="abs quote">It is a long established fact that a reader will be distracted by the readable content of a page when looking at its layout. The point of using Lorem Ipsum is that it has a more-or-less normal distribution of letters, as opposed to using 'Content here, content here', making it look like readable English. Many desktop publishing packages and web page editors now use Lorem Ipsum as their default model text, and a search...</p>
<div class="abs qmark" style="left:948px;top:1880px">&rdquo;</div>
<svg class="abs slide-arrow" style="left:148px" width="12" height="26" viewBox="0 0 12 26"><path d="M11 1L2 13l9 12" fill="none" stroke="#8a9096" stroke-width="1.2"/></svg>
<svg class="abs slide-arrow" style="left:1040px" width="12" height="26" viewBox="0 0 12 26"><path d="M1 1l9 12-9 12" fill="none" stroke="#8a9096" stroke-width="1.2"/></svg>
<div class="abs avatar" role="img" aria-label="Portrait photo of the client"></div>
<div class="abs author">Milo Hensley<br><em>Posted on 27 march 2014</em></div>

<footer class="abs site-footer"></footer>
<div class="abs footer-brand">
  <div class="brand-mark"></div>
  <div class="brand-name">KHCS</div>
</div>
<div class="abs footer-sep"></div>
<div class="abs footer-links">Home<span>|</span>About Us<span>|</span>Services<span>|</span>Technology<span>|</span>Faq<span>|</span>Support<span>|</span>Contact us</div>
<div class="abs copyright">Copyrights &copy; 2014. KHCS. All Rights Reserved</div>
<div class="abs social" style="left:839px"></div>
<div class="abs social" style="left:888px"></div>
<div class="abs social" style="left:936px"></div>
<div class="abs social" style="left:986px"></div>

</body>
</html>
```